Towing Company Website Towing Basel West

Hello I need a cool website for my towing company. - Home - About us - Parking Enforcement - Repossession - Disaster Recovery - Accident Recovery - Contact So someone would have to install the website on Hostwerk for me. No idea how that works.

Target Market(s)

www.bergungsdienst-talwald.cc

Contact Information for Business Card

Bergungsdienst Talwald Ost
P: 044 927 64 18
F: 044 927 64 19
E: mail@bergungsdienst-talwald.cc
W: www.bergungsdienst-talwald.cc

Lukas Brändle
M: 075 638 49 70

Number of Pages Required

5+ page

Font styles to use
Sans Serif

Colors

Designer to choose colors to be used in the design.

```html
<!DOCTYPE html>
<html lang="de">
<head>
<meta charset="utf-8">
<title>Towing Basel West – Bergungsdienst Talwald Ost</title>
<link href="https://fonts.googleapis.com/css2?family=Poppins:wght@300;400;500;600;700&display=swap" rel="stylesheet">
<style>
:root{
  --navy:#3e4a66;
  --navy-dark:#333d55;
  --orange:#f7941d;
  --text:#555b66;
  --heading:#3a3f4a;
  --light:#f1f2f5;
  --white:#ffffff;
  --line:#dcdfe5;
}
*{box-sizing:border-box;margin:0;padding:0}
html,body{width:1200px;height:4244px;overflow:hidden}
body{font-family:"Poppins",sans-serif;color:var(--text);background:var(--white);font-size:13px;line-height:1.6}
a{color:inherit;text-decoration:none}
.wrap{width:920px;margin:0 auto;position:relative}
.btn{display:inline-block;background:var(--orange);color:var(--white);border-radius:20px;font-weight:500;font-size:14px;padding:8px 24px}
.section-title{font-size:30px;font-weight:500;color:var(--heading);text-align:center}
.ph{display:block}

/* top notice */
.notice{height:40px;line-height:40px;text-align:center;color:var(--orange);font-size:13px}

/* header */
.header{height:80px}
.header .wrap{display:flex;align-items:center;justify-content:space-between;height:80px}
.brand{display:flex;align-items:center;gap:10px;font-weight:600;font-size:18px;color:var(--navy)}
.brand .mark{width:22px;height:22px;background:var(--orange)}
.header-contact{display:flex;gap:34px;font-size:13px;color:var(--heading)}
.header-contact span{display:flex;align-items:center;gap:8px}

/* nav */
.nav{height:32px;background:var(--navy)}
.nav ul{list-style:none;display:flex;height:32px;align-items:stretch;width:920px;margin:0 auto;justify-content:space-between}
.nav li{color:var(--white);font-size:13px;display:flex;align-items:center;padding:0 14px}
.nav li.active{background:var(--orange)}

/* hero */
.hero{position:relative;height:528px;background:linear-gradient(180deg,#8a9aa8 0%,#5d6b5a 45%,#4a4d47 100%)}
.hero-copy{position:absolute;left:0;right:0;top:388px;text-align:center}
.hero h1{color:var(--white);font-size:42px;font-weight:600;margin-bottom:18px}

/* features */
.features{height:80px;background:var(--navy)}
.features .wrap{display:flex;justify-content:space-around;align-items:center;height:80px;color:var(--white);font-size:16px;font-weight:500}
.features span{display:flex;align-items:center;gap:12px}

/* about */
.about{height:400px;background:var(--light);padding-top:60px}
.about .wrap{display:flex;gap:40px}
.about-text{width:540px}
.about h2{font-size:30px;font-weight:500;color:var(--heading);margin-bottom:10px}
.about p{font-size:12px;margin-bottom:16px}
.about .btn{font-size:12px;padding:5px 16px}
.about-photo{width:340px;height:160px;margin-top:58px;background:linear-gradient(135deg,#4b5668,#9aa4ae)}

/* services */
.services{height:440px;background:var(--white);padding-top:70px}
.services .wrap{display:flex;justify-content:space-between}
.card{width:286px;background:var(--white);box-shadow:0 2px 10px rgba(0,0,0,.12);text-align:center;padding-bottom:22px}
.card .ph{height:176px;background:linear-gradient(135deg,#5b6470,#aab3bb)}
.card h3{font-size:16px;font-weight:500;color:var(--heading);margin:14px 0 8px}
.card p{font-size:11px;padding:0 26px;margin-bottom:8px}
.card a{color:var(--orange);font-size:11px}

/* accident */
.accident{height:340px;padding-top:20px}
.accident .wrap{display:flex;background:var(--light);height:312px}
.accident-text{width:460px;padding:46px 30px}
.accident h2{font-size:26px;font-weight:500;color:var(--heading);display:flex;align-items:center;gap:14px;margin-bottom:10px}
.accident p{font-size:12px;margin-bottom:12px}
.link{color:var(--navy);font-weight:500;font-size:13px;border-bottom:2px solid var(--orange)}
.accident .ph{width:460px;height:312px;background:linear-gradient(135deg,#5a6a50,#d59a3a 60%,#9aa0a4)}

/* parking */
.parking{height:340px}
.parking .wrap{display:flex;background:var(--light);height:312px}
.parking .ph{width:460px;height:312px;background:linear-gradient(135deg,#2c2e30,#5a5c5e)}
.parking-text{width:460px;padding:40px 30px}
.parking h2{font-size:24px;font-weight:500;color:var(--heading);margin:8px 0 6px}
.parking p{font-size:12px;margin-bottom:12px}

/* facts */
.facts{height:400px;padding-top:60px}
.facts-row{display:flex;justify-content:space-between;width:820px;margin:60px auto 0}
.fact{width:200px;text-align:center}
.circle{width:160px;height:160px;border-radius:50%;border:2px solid var(--line);margin:0 auto 16px;display:flex;align-items:center;justify-content:center;font-size:40px;color:var(--orange);font-weight:500;box-shadow:inset 0 0 0 10px #f6f7f9}
.fact p{font-size:16px;font-weight:500;color:var(--heading)}
.tri{margin-top:50px}

/* call */
.call{height:220px;background:var(--navy);text-align:center;color:var(--white);padding-top:44px}
.call h3{font-size:24px;font-weight:500}
.call .big{font-size:58px;font-weight:300;color:#c9cfdb;line-height:1.2}
.call .big b{color:var(--white);font-weight:400}
.call .btn{margin-top:6px}

/* news */
.news{height:380px;padding-top:110px}
.news-row{display:flex;justify-content:space-between;margin-top:34px}
.post{width:450px;display:flex;gap:14px}
.post .ph{width:120px;height:110px;flex:none;background:linear-gradient(135deg,#cfd4da,#8e969e)}
.post h4{font-size:14px;font-weight:500;color:var(--heading);margin-bottom:4px}
.post p{font-size:11px}
.post p a{color:var(--orange)}
.dots{display:flex;gap:6px;justify-content:center;margin-top:22px}
.dots i{width:8px;height:8px;border-radius:50%;background:#aab}
.dots i.on{background:var(--navy)}

/* inquiry */
.inquiry{height:344px;background:var(--light);padding-top:0}
.inquiry-box{width:600px;margin:0 auto;background:var(--white);position:relative;top:-30px;padding:24px 40px 24px;box-shadow:0 2px 12px rgba(0,0,0,.08)}
.inquiry h2{font-size:28px;font-weight:500;color:var(--heading);text-align:center;margin-bottom:18px}
.fields{display:grid;grid-template-columns:1fr 1fr;gap:14px 20px}
.field{height:34px;border:1px solid var(--line);font-size:12px;color:#999;display:flex;align-items:center;padding:0 12px;gap:8px}
.field.full{grid-column:1/3;height:70px;align-items:flex-start;padding-top:8px}
.inquiry .submit{text-align:center;margin-top:16px}

/* footer */
.footer{height:320px;background:var(--navy);color:#d5d9e2;padding-top:46px}
.footer .wrap{display:flex;gap:60px}
.footer h5{color:var(--white);font-size:14px;font-weight:500;margin-bottom:14px}
.footer ul{list-style:none;font-size:12px;line-height:2}
.footer li::before{content:"› ";color:var(--orange)}
.contact-list li::before{content:""}
.contact-list li{display:flex;gap:8px;align-items:flex-start;line-height:1.5;margin-bottom:8px}
.dl p{font-size:12px;line-height:1.8}
.dl .btn{font-size:11px;padding:4px 14px;margin-top:10px}
.foot-brand{margin-left:auto;color:var(--white);font-weight:600;font-size:15px;display:flex;gap:8px;align-items:center}
.foot-brand .mark{width:18px;height:18px;background:var(--orange)}

/* bottom */
.bottom{height:44px;background:var(--navy-dark);border-top:1px solid #4c5876}
.bottom .wrap{display:flex;justify-content:space-between;align-items:center;height:44px;font-size:11px;color:var(--orange)}
.social{display:flex;gap:8px}
.social i{width:22px;height:22px;border-radius:50%;background:#cfd4de}
</style>
</head>
<body>

<div class="notice">Wrong parked? We calculate directly with the parker!</div>

<header class="header">
  <div class="wrap">
    <div class="brand"><span class="mark"></span>Bergungsdienst Talwald Ost</div>
    <div class="header-contact">
      <span><svg width="16" height="16" viewBox="0 0 24 24"><path fill="#3e4a66" d="M6.6 10.8a15 15 0 0 0 6.6 6.6l2.2-2.2c.3-.3.7-.4 1-.2 1.1.4 2.3.6 3.6.6.6 0 1 .4 1 1V20c0 .6-.4 1-1 1A17 17 0 0 1 3 4c0-.6.4-1 1-1h3.5c.6 0 1 .4 1 1 0 1.3.2 2.5.6 3.6.1.3 0 .7-.2 1z"/></svg>044 927 64 18</span>
      <span><svg width="16" height="16" viewBox="0 0 24 24"><rect x="2" y="5" width="20" height="14" rx="2" fill="none" stroke="#3e4a66" stroke-width="2"/><path d="M2 6l10 7 10-7" fill="none" stroke="#3e4a66" stroke-width="2"/></svg>mail@bergungsdienst-talwald.cc</span>
    </div>
  </div>
</header>

<nav class="nav">
  <ul>
    <li class="active">Home</li><li>About Us</li><li>Parking Enforcement</li><li>Repossession</li><li>Breakdown Assistance</li><li>Accident Recovery</li><li>Contact Us</li>
  </ul>
</nav>

<section class="hero">
  <div class="ph" role="img" aria-label="Photo of yellow tow trucks parked in a row" style="position:absolute;inset:0"></div>
  <div class="hero-copy">
    <h1>Schlepper für Falschparker im Einsatz</h1>
    <a class="btn" href="#">Contact Us Today</a>
  </div>
</section>

<section class="features">
  <div class="wrap">
    <span><svg width="30" height="24" viewBox="0 0 30 24"><circle cx="9" cy="7" r="4" fill="#fff"/><circle cx="21" cy="7" r="4" fill="#fff"/><path d="M1 22c0-5 4-8 8-8s8 3 8 8zM13 22c0-5 4-8 8-8s8 3 8 8z" fill="#fff"/></svg>We Have Trained Staff</span>
    <span><svg width="26" height="26" viewBox="0 0 26 26"><circle cx="13" cy="13" r="11" fill="none" stroke="#fff" stroke-width="2"/><text x="13" y="17" font-size="9" text-anchor="middle" fill="#fff" font-family="Poppins,sans-serif">24</text></svg>24/7 Services</span>
    <span><svg width="26" height="26" viewBox="0 0 26 26"><path d="M3 3h10l10 10-10 10L3 13z" fill="none" stroke="#fff" stroke-width="2"/><circle cx="8" cy="8" r="2" fill="#fff"/></svg>Our Prices are Affordable</span>
  </div>
</section>

<section class="about">
  <div class="wrap">
    <div class="about-text">
      <h2>About Us</h2>
      <p>Lorem ipsum dolor sit amet, consectetuer adipiscing elit, sed diam nonummy nibh euismod tincidunt ut laoreet dolore magna aliquam erat volutpat. Ut wisi enim ad minim veniam, quis nostrud exerci tation ullamcorper suscipit lobortis nisl ut aliquip ex ea commodo consequat.</p>
      <p>Duis autem vel eum iriure dolor in hendrerit in vulputate velit esse molestie consequat, vel illum dolore eu feugiat nulla facilisis at vero eros et accumsan et iusto odio dignissim qui blandit praesent luptatum zzril delenit augue duis dolore te feugait nulla facilisi.</p>
      <a class="btn" href="#">Read More</a>
    </div>
    <div class="about-photo ph" role="img" aria-label="Photo of a car being lifted onto a tow truck"></div>
  </div>
</section>

<section class="services">
  <div class="wrap">
    <article class="card">
      <div class="ph" role="img" aria-label="Photo of a tow truck driver at work"></div>
      <h3>Parking Enforcement</h3>
      <p>Duis autem vel eum iriure dolor in hendrerit in vulputate velit esse molestie consequat, vel illum dolore eu feugiat nulla facilisis at vero eros.</p>
      <a href="#">Continue Reading →</a>
    </article>
    <article class="card">
      <div class="ph" role="img" aria-label="Photo of a car loaded on a recovery truck"></div>
      <h3>Repossession</h3>
      <p>Duis autem vel eum iriure dolor in hendrerit in vulputate velit esse molestie consequat, vel illum dolore eu feugiat nulla facilisis at vero eros.</p>
      <a href="#">Continue Reading →</a>
    </article>
    <article class="card">
      <div class="ph" role="img" aria-label="Photo of a broken-down car at the roadside"></div>
      <h3>Breakdown Assistance</h3>
      <p>Duis autem vel eum iriure dolor in hendrerit in vulputate velit esse molestie consequat, vel illum dolore eu feugiat nulla facilisis at vero eros.</p>
      <a href="#">Continue Reading →</a>
    </article>
  </div>
</section>

<section class="accident">
  <div class="wrap">
    <div class="accident-text">
      <h2><svg width="62" height="34" viewBox="0 0 62 34"><rect x="2" y="10" width="22" height="14" fill="#3a3f4a"/><path d="M24 14h10l6 8v2H24z" fill="#3a3f4a"/><path d="M38 4l22 14" stroke="#3a3f4a" stroke-width="3"/><circle cx="10" cy="27" r="5" fill="#3a3f4a"/><circle cx="32" cy="27" r="5" fill="#3a3f4a"/></svg>Accident Recovery</h2>
      <p>Duis autem vel eum iriure dolor in hendrerit in vulputate velit esse molestie consequat, vel illum dolore eu feugiat nulla facilisis at vero eros et accumsan et iusto odio dignissim qui blandit. Duis autem vel eum iriure dolor in hendrerit.</p>
      <a class="link" href="#">Arrange An Appointment With Us!</a>
    </div>
    <div class="ph" role="img" aria-label="Photo of a yellow flatbed truck carrying a damaged car"></div>
  </div>
</section>

<section class="parking">
  <div class="wrap">
    <div class="ph" role="img" aria-label="Photo of a private parking space marked on asphalt"></div>
    <div class="parking-text">
      <svg width="40" height="40" viewBox="0 0 40 40"><rect x="4" y="4" width="26" height="26" rx="3" fill="#3a3f4a"/><text x="17" y="24" font-size="18" font-weight="700" text-anchor="middle" fill="#fff" font-family="Poppins,sans-serif">P</text><rect x="16" y="30" width="3" height="9" fill="#3a3f4a"/></svg>
      <h2>Free parking!</h2>
      <p>We monitor your parking around the clock. We are where wrong, foreign or long-term parkers are a problem – we solve them immediately. With our service, we ensure the satisfaction of customers.</p>
      <a class="link" href="#">Arrange An Appointment With Us!</a>
    </div>
  </div>
</section>

<section class="facts">
  <h2 class="section-title">Quick Facts</h2>
  <div class="facts-row">
    <div class="fact"><div class="circle">325</div><p>Lorem Ipsum dummy text</p></div>
    <svg class="tri" width="50" height="40" viewBox="0 0 50 40"><path d="M4 36L30 4" stroke="#f7941d" stroke-width="3" fill="none"/><path d="M4 36h44" stroke="#f7941d" stroke-width="3"/></svg>
    <div class="fact"><div class="circle">45</div><p>Lorem Ipsum dummy text</p></div>
    <svg class="tri" width="50" height="40" viewBox="0 0 50 40"><path d="M4 36L30 4" stroke="#f7941d" stroke-width="3" fill="none"/><path d="M4 36h44" stroke="#f7941d" stroke-width="3"/></svg>
    <div class="fact"><div class="circle">21</div><p>Lorem Ipsum dummy text</p></div>
  </div>
</section>

<section class="call">
  <h3>Towing Basel West likes to help in any situation</h3>
  <div class="big">Call 044.927.6418 <b>or</b></div>
  <a class="btn" href="#">Contact Us Today</a>
</section>

<section class="news">
  <div class="wrap">
    <h2 class="section-title">Latest News</h2>
    <div class="news-row">
      <article class="post">
        <div class="ph" role="img" aria-label="News thumbnail photo"></div>
        <div><h4>Duis autem vel eum iriure</h4><p>Duis autem vel eum iriure dolor in hendrerit in vulputate velit esse molestie consequat, vel illum dolore eu feugiat nulla facilisis at vero eros et accumsan vel eum iriure dolor in hendrerit … <a href="#">Read More</a></p></div>
      </article>
      <article class="post">
        <div class="ph" role="img" aria-label="News thumbnail photo"></div>
        <div><h4>Duis autem vel eum iriure</h4><p>Duis autem vel eum iriure dolor in hendrerit in vulputate velit esse molestie consequat, vel illum dolore eu feugiat nulla facilisis at vero eros et accumsan vel eum iriure dolor in hendrerit … <a href="#">Read More</a></p></div>
      </article>
    </div>
    <div class="dots"><i></i><i class="on"></i><i></i><i></i></div>
  </div>
</section>

<section class="inquiry">
  <div class="inquiry-box">
    <h2>Quick Inquiry</h2>
    <div class="fields">
      <div class="field">👤 First Name*</div>
      <div class="field">👤 Last Name*</div>
      <div class="field">☎ Your Phone*</div>
      <div class="field">✉ Your Email*</div>
      <div class="field full">✎ Your Message*</div>
    </div>
    <div class="submit"><a class="btn" href="#">Submit</a></div>
  </div>
</section>

<footer class="footer">
  <div class="wrap">
    <div>
      <h5>Quick Links</h5>
      <ul><li>Home</li><li>About Us</li><li>Parking Enforcement</li><li>Repossession</li><li>Breakdown Assistance</li><li>Accident Recovery</li><li>Contact Us</li></ul>
    </div>
    <div>
      <h5>Contact Details</h5>
      <ul class="contact-list">
        <li><span style="color:var(--orange)">●</span><span>Towing Basel West<br>Talwaldstrasse 14<br>4055 Basel</span></li>
        <li><span style="color:var(--orange)">●</span><span>mail@bergungsdienst-talwald.cc</span></li>
        <li><span style="color:var(--orange)">●</span><span>044 927 64 18</span></li>
      </ul>
    </div>
    <div class="dl">
      <h5>Downloads</h5>
      <p>Datenblatt Parkkontrolle<br>Tarife für private Parkplätze<br>Formular Auftragserteilung</p>
      <a class="btn" href="#">Download PDF</a>
    </div>
    <div class="foot-brand"><span class="mark"></span>Bergungsdienst Talwald Ost</div>
  </div>
</footer>

<div class="bottom">
  <div class="wrap">
    <span>Copyright © 2021 Towing Basel West. All rights reserved.</span>
    <div class="social"><i></i><i></i><i></i></div>
  </div>
</div>

</body>
</html>
```